New company that wants to specialize in presale property and garden do ups

I own A landscaping and premium garden maintenance company.
I want to advertise to people that are listing there homes for sale.
For the purpose of using my company services to fix up there home and gardens to maximize there sale potential. I am on instagram as trvbloom_landscaping. I am aiming for the higher end of the market. This Flyer will be post card size. I would like my logo to be used. And your layout to be clean cut and easy to read. I need my clients to understand that spending time on there gardens appearance will aid with sale of there home and maximize there profit
Target Market(s)
People selling there homes. or thinking about selling there homes
Industry/Entity Type
Landscape Gardening
Requirements
Must have
- Email address neil@trvbloom.co.nz number 0218463307 and the instagram logo
- The benefits of spending money of the look and feel of gardens to maximize there chance of quick and profitable sale. wow factor and so on. Free estimate no obligation
Nice to have
- Any thing you can add to the layout that would help as sound professional and get our point across.

```html
<!DOCTYPE html>
<html lang="en">
<head>
<meta charset="utf-8">
<title>TRVBLOOM Landscaping – Presale Garden Flyer</title>
<link rel="stylesheet" href="https://fonts.googleapis.com/css2?family=Open+Sans:wght@400;700&family=Nunito:wght@700;900&display=swap">
<style>
  :root{
    --wall-dark:#2b2d2f;
    --wall-mid:#4a4d4f;
    --lawn:#9ccb3b;
    --lawn-light:#b4dc52;
    --lawn-deep:#7fb52a;
    --ink-blue:#0f4c9c;
    --soft-blue:#1a5fb4;
    --white:#ffffff;
    --ring-green:#8cc63f;
    --mark-black:#111111;
  }
  *{margin:0;padding:0;box-sizing:border-box}
  html,body{width:1200px;height:849px;overflow:hidden;background:var(--white)}
  .flyer{position:relative;width:1200px;height:849px;overflow:hidden;font-family:"Open Sans",Arial,sans-serif;color:var(--white)}
  .room-backdrop{position:absolute;inset:0;
    background:
      radial-gradient(ellipse 260px 220px at 215px 740px, rgba(255,255,255,.85), rgba(255,255,255,0) 70%),
      linear-gradient(180deg,var(--wall-dark) 0%,var(--wall-mid) 32%,#5f7140 48%,var(--lawn-deep) 58%,var(--lawn) 72%,var(--lawn-light) 100%);}
  .intro{position:absolute;left:262px;top:101px;font-size:27.5px;line-height:40px;letter-spacing:-.2px;white-space:nowrap}
  .intro p{margin-bottom:15px}
  .intro strong{font-weight:700}
  .badge{position:absolute;border-radius:50%;background:linear-gradient(160deg,#fff6ec,#f4a46b 60%,#e9f0f5);border:5px solid var(--ring-green);box-shadow:0 3px 10px rgba(0,0,0,.35);z-index:1}
  .badge--house{left:775px;top:60px;width:128px;height:128px}
  .badge--savings{left:827px;top:452px;width:178px;height:178px;background:linear-gradient(160deg,#ffffff,#f6c343 55%,#8a4a2a)}
  .headline{position:absolute;z-index:2;left:205px;top:382px;white-space:nowrap;font-family:"Nunito","Arial Rounded MT Bold",sans-serif;font-weight:700;font-size:68px;line-height:72px;letter-spacing:-1.2px;color:var(--soft-blue);
    text-shadow:-3px -3px 0 var(--white),3px -3px 0 var(--white),-3px 3px 0 var(--white),3px 3px 0 var(--white),0 -3px 0 var(--white),0 3px 0 var(--white),-3px 0 0 var(--white),3px 0 0 var(--white),4px 6px 8px rgba(0,0,0,.35)}
  .headline b{font-weight:900;color:var(--ink-blue)}
  .brand{position:absolute;left:140px;top:700px;width:150px;text-align:center;color:var(--mark-black);font-weight:700;font-size:22px;line-height:26px;letter-spacing:.5px}
  .brand-dot{display:block;width:40px;height:40px;border-radius:50%;background:var(--mark-black);margin:0 auto 8px}
  .contact{position:absolute;top:688px;text-align:center;font-size:23.5px;white-space:nowrap}
  .contact svg{display:block;margin:0 auto 14px}
  .contact--social{left:332px;width:252px}
  .contact--email{left:625px;width:252px}
  .contact--phone{left:915px;width:130px}
</style>
</head>
<body>
<main class="flyer">
  <div class="room-backdrop" role="img" aria-label="Empty room with dark brick walls, arched window and pendant lamps fading into green lawn"></div>

  <section class="intro">
    <p>Are you <strong>listing your home for sale?</strong></p>
    <p>Do you want to <strong>fix up your home<br>and gardens to maximize your sale potential?</strong></p>
    <p>Do you know <strong>spending time on your gardens appearance</strong> will<br>aid the <strong>sale of your home</strong> and <strong>maximize your profit.</strong></p>
  </section>

  <div class="badge badge--house" role="img" aria-label="Illustration of a house with orange roof and a tree"></div>

  <h1 class="headline">Are you <b>selling your home</b><br>or <b>thinking</b> about<br><b>selling your home</b>?</h1>

  <div class="badge badge--savings" role="img" aria-label="Illustration of a hand dropping coins into a house"></div>

  <div class="brand"><span class="brand-dot"></span>TRVBLOOM LANDSCAPING</div>

  <div class="contact contact--social">
    <svg width="38" height="38" viewBox="0 0 38 38" aria-hidden="true"><circle cx="19" cy="19" r="17" fill="none" stroke="var(--ink-blue)" stroke-width="2.5"/></svg>
    trvbloom_landscaping
  </div>
  <div class="contact contact--email">
    <svg width="38" height="38" viewBox="0 0 38 38" aria-hidden="true"><circle cx="19" cy="19" r="17" fill="none" stroke="var(--ink-blue)" stroke-width="2.5"/><rect x="10" y="13" width="18" height="12" rx="1.5" fill="var(--ink-blue)"/><path d="M10.5 13.5 19 20.5 27.5 13.5" fill="none" stroke="var(--lawn)" stroke-width="1.6"/></svg>
    neil@trvbloom.co.nz
  </div>
  <div class="contact contact--phone">
    <svg width="38" height="38" viewBox="0 0 38 38" aria-hidden="true"><circle cx="19" cy="19" r="17" fill="none" stroke="var(--ink-blue)" stroke-width="2.5"/><path d="M13 11c1-1 2-1 2.6 0l2 3c.5.8.3 1.6-.4 2.2l-1.2 1c.8 2 2.4 3.6 4.4 4.4l1-1.2c.6-.7 1.4-.9 2.2-.4l3 2c1 .6 1 1.6 0 2.6l-1.4 1.4c-1.2 1.2-3.4 1.2-6-.4-3.4-2-6-4.6-8-8-1.6-2.6-1.6-4.8-.4-6z" fill="var(--ink-blue)"/></svg>
    0218463307
  </div>
</main>
</body>
</html>
```